Business Card and Logo tweak for a Language Boarding School

we are a boadring langauge school for under 18 international student.
We call ourselves " HCSC" - Harwick Crossway Study Centre
We are one of the TQ "tidewater quarters" Melbourne campus for TQ high school preparation program.

our address is 14 Orrin Lane Brighton 3187
Ph: 03 95550142
Email: info@myhcsc-example.com
Website: www.myhcsc-example.com

We have our HCSC logo, but not very satisfied. May be you can tweak it furhter with the fond or formations.

Basically the business card list all relevant info on one side and list all our programs on the other side.

The program we have:
ELICOS with Boarding for U18 Students
HSP-High School Preparation Program
PSP- Primary School Preparation Program
Junior Holiday Program & Study Tours
After School Tutoring
Student Wellbeing and Counselling

```html
<!DOCTYPE html>
<html lang="en">
<head>
<meta charset="utf-8">
<title>Harwick Crossway Study Centre – Business Card</title>
<link rel="stylesheet" href="https://fonts.googleapis.com/css2?family=Raleway:wght@400;500&family=Oswald:wght@400;500&display=swap">
<style>
  :root {
    --bg: #3a3a3a;
    --paper: #ffffff;
    --ink: #1f1f1f;
    --dark-card: #1e1e1e;
    --light-text: #ffffff;
    --rule: #8a8a8a;
    --cyan: #0ff0e6;
    --green: #a8e22c;
    --red: #f0164c;
    --orange: #f9a414;
    --purple: #4b1a8c;
  }
  * { box-sizing: border-box; margin: 0; padding: 0; }
  html, body { width: 1200px; height: 1200px; overflow: hidden; }
  body {
    background: var(--bg);
    font-family: "Raleway", sans-serif;
    position: relative;
  }
  .card {
    position: absolute;
    left: 160px;
    width: 880px;
    height: 503px;
    border-radius: 36px;
    overflow: hidden;
    box-shadow: 0 18px 40px rgba(0,0,0,.45);
  }
  .card--programs { top: 60px; background: var(--paper); color: var(--ink); }
  .card--contact { top: 630px; background: var(--dark-card); color: var(--light-text); }

  .brand {
    position: absolute;
    display: flex;
    align-items: center;
    gap: 34px;
  }
  .card--programs .brand { left: 120px; top: 50px; }
  .card--contact .brand { left: 150px; top: 70px; }
  .brand-dot {
    width: 120px; height: 120px; border-radius: 50%;
    background: currentColor;
    flex: none;
  }
  .brand-name {
    font-family: "Raleway", sans-serif;
    font-weight: 500;
    font-size: 44px;
    line-height: 1.02;
    text-transform: uppercase;
    letter-spacing: 1px;
  }

  .programs {
    position: absolute;
    left: 60px; right: 60px; top: 270px;
    text-align: center;
  }
  .programs-title {
    font-family: "Raleway", sans-serif;
    font-weight: 500;
    font-size: 24px;
    letter-spacing: 1px;
    padding-bottom: 10px;
  }
  .programs-rule { height: 1px; background: var(--rule); margin-bottom: 16px; }
  .program-list {
    list-style: none;
    font-family: "Oswald", sans-serif;
    font-weight: 400;
    font-size: 22px;
    line-height: 1.4;
    text-transform: uppercase;
  }
  .program-list li { display: inline; }
  .program-list li::before {
    content: "";
    display: inline-block;
    width: 8px; height: 8px; border-radius: 50%;
    margin: 0 8px 3px 14px;
    background: var(--bullet);
    vertical-align: middle;
  }
  .colour-band {
    position: absolute; left: 0; right: 0; bottom: 0; height: 22px;
    display: flex;
  }
  .colour-band span { flex: 1; }
  .colour-band .cyan { background: var(--cyan); }
  .colour-band .green { background: var(--green); }
  .colour-band .red { background: var(--red); }
  .colour-band .orange { background: var(--orange); flex: .6; }

  .contacts {
    position: absolute;
    left: 130px; right: 70px; bottom: 60px;
    display: flex; justify-content: space-between;
    font-size: 24px; font-weight: 400;
  }
  .contact-group p { display: flex; align-items: center; gap: 12px; margin-top: 10px; }
  .contact-group svg { width: 24px; height: 24px; flex: none; fill: none; stroke: var(--light-text); stroke-width: 2; }
</style>
</head>
<body>

<section class="card card--programs">
  <div class="brand">
    <span class="brand-dot" aria-hidden="true"></span>
    <div class="brand-name">Harwick<br>Crossway<br>Study<br>Centre</div>
  </div>
  <div class="programs">
    <h2 class="programs-title">OUR PROGRAMS</h2>
    <div class="programs-rule"></div>
    <ul class="program-list">
      <li style="--bullet: var(--green)">ELICOS with Boarding for U18 Students</li>
      <li style="--bullet: var(--orange)">HSP-High School Preparation Program</li><br>
      <li style="--bullet: var(--purple)">PSP- Primary School Preparation Program</li>
      <li style="--bullet: var(--cyan)">Junior Holiday Program &amp; Study Tours</li><br>
      <li style="--bullet: var(--red)">After School Tutoring</li>
      <li style="--bullet: var(--green)">Student Wellbeing and Counselling</li>
    </ul>
  </div>
  <div class="colour-band" aria-hidden="true">
    <span class="cyan"></span><span class="green"></span><span class="red"></span><span class="orange"></span>
  </div>
</section>

<section class="card card--contact">
  <div class="brand">
    <span class="brand-dot" aria-hidden="true"></span>
    <div class="brand-name">Harwick<br>Crossway<br>Study<br>Centre</div>
  </div>
  <div class="contacts">
    <div class="contact-group">
      <p>
        <svg viewBox="0 0 24 24" aria-hidden="true"><path d="M5 3h4l2 5-3 2a12 12 0 0 0 6 6l2-3 5 2v4a2 2 0 0 1-2 2A17 17 0 0 1 3 5a2 2 0 0 1 2-2z"/></svg>
        03 95550142
      </p>
      <p>
        <svg viewBox="0 0 24 24" aria-hidden="true"><rect x="2" y="5" width="20" height="14"/><path d="M2 5l10 8 10-8"/></svg>
        info@myhcsc-example.com
      </p>
    </div>
    <div class="contact-group">
      <p>
        <svg viewBox="0 0 24 24" aria-hidden="true"><circle cx="12" cy="12" r="10"/><path d="M2 12h20M12 2c3 3 3 17 0 20M12 2c-3 3-3 17 0 20"/></svg>
        www.myhcsc-example.com
      </p>
      <p>
        <svg viewBox="0 0 24 24" aria-hidden="true"><path d="M12 22s7-7 7-12a7 7 0 0 0-14 0c0 5 7 12 7 12z"/><circle cx="12" cy="10" r="2.5"/></svg>
        14 Orrin Lane Brighton 3187
      </p>
    </div>
  </div>
</section>

</body>
</html>
```